VKT other templates

1) Internal pages for the documents that we write. basically what will the pages inside look like. It should basically be a document with a header, a footer and a page number locator. It should include the following information: name of the report, date, VKT logo somehow, and version (draft, final etc). the information should be divided between header and footer. let me know if its unclear. As with everything it should work both in black and white and in color in case it is printed in black and white :-)
2) chapter dividers. This are the pages that you might have inside the report to separate sections. It should just have a page number, and chapter or section name. Simple, but again follow the same idea of the design that you created. It should be possible to have a picture in the divider, but it should not be a must. so in that sense we need to versions.
3) Business cards. Should include space for name, title, phone numbers (2 or 3), email, Skype, web page, and the company address which you have already.
4) a signature for emails. Basically the file that is glued to the bottom off all emails as a signature. Again it should include all the information in the business cards.

Not including any files since you have already designed others

```html
<!DOCTYPE html>
<html lang="en">
<head>
<meta charset="utf-8">
<title>VKT – Internal Report Page</title>
<link href="https://fonts.googleapis.com/css2?family=Exo+2:wght@300;400&display=swap" rel="stylesheet">
<style>
  :root {
    --backdrop: #cdd9dc;
    --paper: #f4f4f4;
    --wave-tone: rgba(201, 214, 225, 0.75);
    --wave-fade: rgba(201, 214, 225, 0);
    --ink: #5f7f95;
    --ink-soft: #8aa2b3;
  }
  html, body {
    margin: 0;
    width: 1200px;
    height: 1000px;
    overflow: hidden;
    background: var(--backdrop);
    font-family: "Exo 2", sans-serif;
  }
  .report-page {
    position: absolute;
    left: 282px;
    top: 50px;
    width: 636px;
    height: 900px;
    background: var(--paper);
    box-shadow: 0 6px 24px rgba(60, 80, 90, 0.18);
    overflow: hidden;
  }
  .header-wave {
    position: absolute;
    top: 0;
    left: 0;
    width: 636px;
    height: 150px;
    background: linear-gradient(165deg, var(--wave-fade) 0%, var(--wave-fade) 35%, var(--wave-tone) 100%);
  }
  .footer-wave {
    position: absolute;
    bottom: 0;
    left: 0;
    width: 636px;
    height: 150px;
    background: linear-gradient(-15deg, var(--wave-fade) 0%, var(--wave-fade) 35%, var(--wave-tone) 100%);
    opacity: 0.8;
  }
  .header-brand {
    position: absolute;
    top: 150px;
    right: 34px;
    text-align: center;
    color: var(--ink);
  }
  .brand-name {
    font-size: 30px;
    font-weight: 400;
    letter-spacing: 1px;
    line-height: 1;
  }
  .document-version {
    font-size: 10px;
    font-weight: 300;
    letter-spacing: 1px;
    margin-top: 2px;
  }
  .footer-details {
    position: absolute;
    left: 30px;
    bottom: 108px;
    color: var(--ink-soft);
    font-size: 10px;
    font-weight: 300;
    line-height: 1.35;
  }
  .page-number {
    position: absolute;
    right: 40px;
    bottom: 34px;
    color: var(--ink-soft);
    font-size: 15px;
    font-weight: 300;
    letter-spacing: 2px;
  }
</style>
</head>
<body>
  <main class="report-page">
    <div class="header-wave" role="img" aria-label="Soft light-blue wave ornament across the page header"></div>
    <div class="footer-wave" role="img" aria-label="Soft light-blue wave ornament across the page footer"></div>

    <header class="header-brand">
      <div class="brand-name">VKT</div>
      <div class="document-version">-Draft-</div>
    </header>

    <footer class="footer-details">
      <div class="report-title">Social Dialogue in Developing Countries</div>
      <div class="report-date">01.01.2014</div>
    </footer>

    <div class="page-number">- 21 -</div>
  </main>
</body>
</html>
```